Wordpress Design Project

Good day.

I was hoping to buy a professional looking Wordpress template and just fill in the blanks with my personal data and start blogging, but unfortunately my blog posts need to include images that are 756 pixels x 439.

A sample image can be found at.
http://files.brindlecache.net/7-Pics/layoutsample.gif

So, I need your help.

1 This is a daily newsletter / blog site only. Not a corporate site.
2 Subject - Stock Market
2 I have no color preferences. I will leave that up to you.
I would like something that looks like this
http://preview.loftmerath.com/clarity/
3 I would like to include Vortelli Ads on both the Home Page and within each post.
4 The home page should show a link and a short summary to each post.
5 The home page should include an email capture box. We use MailChimp)
6 The home page should include a Site Search Box and function.
7 The home page should include a External Links Box.

If I have forgotten anything, please let me know.
I welcome your suggestions.

I look forward to seeing your designs and picking a winner.

Thank you for reading my post.

Darren Oakhurst

Vortelli

```html
<!DOCTYPE html>
<html lang="en">
<head>
<meta charset="utf-8">
<title>Stock Market</title>
<link href="https://fonts.googleapis.com/css2?family=Open+Sans:ital,wght@0,400;0,600;0,700;1,400&family=PT+Sans:wght@400;700&family=Arimo:wght@400;700&family=Droid+Serif&family=Noto+Serif:ital,wght@0,400;0,700;1,400&display=swap" rel="stylesheet">
<style>
:root{
  --header:#141414;
  --header-hi:#2a2a2a;
  --nav:#ffffff;
  --page:#e8e8e8;
  --card:#f6f6f6;
  --line:#d2d2d2;
  --ink:#2b2b2b;
  --muted:#7a7a7a;
  --faint:#a8a8a8;
  --btn:#1c1c1c;
  --footer:#111111;
  --footer-bar:#0a0a0a;
  --footer-ink:#d8d8d8;
  --accent:#3aa9d8;
  --ad:#8a8a8a;
  --ribbon:#4aa6bf;
}
*{margin:0;padding:0;box-sizing:border-box}
html,body{width:882px;height:1200px;overflow:hidden}
body{position:relative;background:var(--page);font-family:"Open Sans",Arial,sans-serif;color:var(--ink)}
.abs{position:absolute}
.site-header{left:0;top:0;width:882px;height:122px;background:radial-gradient(ellipse at 50% 0,var(--header-hi),var(--header) 70%)}
.site-name{left:0;width:882px;top:36px;text-align:center;color:#fff;font:700 34px/1 "Noto Serif",Georgia,serif;letter-spacing:1px}
.social{top:15px;width:22px;height:22px;border-radius:50%;background:#555;border:2px solid #ddd}
.main-nav{left:0;top:122px;width:882px;height:35px;background:var(--nav);border-bottom:1px solid var(--line)}
.nav-links{position:absolute;left:132px;top:9px;display:flex;gap:11px;white-space:nowrap}
.nav-links a{font:400 11.5px "PT Sans",Arial,sans-serif;color:var(--ink);text-decoration:none}
.search{left:623px;top:6px;width:112px;height:20px;border:1px solid var(--line);border-radius:2px;font:italic 9px "Noto Serif",serif;color:var(--faint);padding:4px 6px;white-space:nowrap}
.dropdown{left:155px;top:157px;width:117px;height:120px;background:#fff;box-shadow:0 2px 6px rgba(0,0,0,.2);z-index:3;padding-top:12px}
.dropdown a{display:block;font-size:8px;color:var(--ink);padding:0 18px;height:21px;line-height:21px;text-decoration:none}
.dropdown a.dim{color:var(--faint)}
.tab{left:386px;top:170px;width:112px;height:22px;background:#f5f5f5;border:1px solid var(--line);border-bottom:none;font-size:7.5px;color:var(--muted);text-align:center;line-height:22px}
.feature-line{left:132px;top:192px;width:603px;height:1px;background:var(--line)}
.chart{background:linear-gradient(180deg,#f2f2f2 0%,#dcdce8 55%,#c9cbe0 75%,#f0f0f0 100%);border:5px solid #fff;box-shadow:0 0 0 1px var(--line)}
.arrow{top:278px}
.feature-title{left:414px;top:222px;font:400 18px Arimo,Arial,sans-serif;white-space:nowrap}
.meta{font:italic 8px "Noto Serif",Georgia,serif;color:var(--faint);white-space:nowrap}
.meta b{color:var(--muted);font-weight:400}
.excerpt{font:400 7.8px/14px "PT Sans",Arial,sans-serif;color:#666;white-space:nowrap;overflow:hidden}
.review-line{left:132px;top:381px;width:603px;height:1px;background:var(--line)}
.pill{background:linear-gradient(#444,var(--btn));color:#fff;border-radius:12px;text-align:center;font:11px "Droid Serif","Noto Serif",serif;box-shadow:0 2px 3px rgba(0,0,0,.35);white-space:nowrap}
.label{font-size:7.5px;color:var(--faint);letter-spacing:.3px;text-transform:uppercase}
.card{width:166px;height:210px;background:var(--card);border:1px solid var(--line)}
.card .chart{position:absolute;left:4px;top:4px;width:156px;height:86px;border-width:3px}
.card h3{position:absolute;left:0;width:164px;top:95px;text-align:center;font:400 13px Arimo,Arial,sans-serif;letter-spacing:.5px;white-space:nowrap}
.card .meta{position:absolute;left:0;width:164px;top:113px;text-align:center}
.card .excerpt{position:absolute;left:21px;width:128px;top:128px;height:58px;font-size:8px}
.card .pill{position:absolute;left:48px;top:196px;width:68px;height:22px;line-height:22px}
.ribbon{left:246px;top:404px;width:60px;height:16px;background:var(--ribbon);color:#fff;font-size:6px;text-align:center;line-height:16px;transform:rotate(45deg);transform-origin:0 0;z-index:2}
.side-rule{left:527px;top:382px;width:1px;height:588px;background:#c8c8c8}
.newsletter{left:541px;top:413px;width:189px;height:168px;background:#fff;border:1px solid var(--line)}
.newsletter h4{position:absolute;left:12px;top:10px;font:400 11px "Noto Serif",serif;white-space:nowrap}
.newsletter .rule{position:absolute;left:0;top:33px;width:187px;height:1px;background:var(--line)}
.newsletter p.intro{position:absolute;left:12px;top:38px;width:165px;font-size:8.5px;line-height:14px;color:#555}
.email{position:absolute;left:12px;top:80px;width:131px;height:21px;border:1px solid var(--line);font-size:8px;color:var(--faint);padding:5px 6px;white-space:nowrap}
.signup{position:absolute;left:120px;top:110px;width:56px;height:22px;background:linear-gradient(#555,#222);color:#fff;font:700 8px "Open Sans",sans-serif;text-align:center;line-height:22px;border-radius:2px}
.spam{position:absolute;left:8px;top:148px;font:italic 6.5px "Noto Serif",serif;color:#555;white-space:nowrap}
.list{list-style:none}
.list li{height:17px;font-size:7.8px;color:var(--ink);padding-left:12px;position:relative;white-space:nowrap}
.list li::before{content:"";position:absolute;left:3px;top:5px;width:2px;height:2px;background:#999}
.list li.dim{color:var(--faint)}
.ad{left:541px;top:840px;width:189px;height:125px;background:var(--ad);color:#fff;font-size:13px;text-align:center;line-height:125px;white-space:nowrap}
.pager{top:923px;width:24px;height:24px;background:#f7f7f7;border:1px solid var(--line);font:700 9px "Droid Serif",serif;text-align:center;line-height:22px}
.site-footer{left:0;top:970px;width:882px;height:230px;background:var(--footer);color:var(--footer-ink)}
.site-footer h5{position:absolute;top:35px;font:600 8px "Open Sans",sans-serif;color:#fff}
.foot-col{position:absolute;top:54px;list-style:none;font-size:8px;white-space:nowrap}
.foot-col li{height:13.5px}
.foot-col.dots li{padding-left:12px;position:relative;height:17.5px}
.foot-col.dots li::before{content:"";position:absolute;left:3px;top:5px;width:2px;height:2px;background:#888}
.footer-bar{position:absolute;left:0;top:190px;width:882px;height:40px;background:var(--footer-bar)}
.footer-links{position:absolute;left:126px;top:13px;display:flex;gap:9px;white-space:nowrap}
.footer-links a{font:700 8.5px "PT Sans",sans-serif;color:#fff;text-decoration:none}
.footer-links a.current{color:var(--accent);font-style:italic}
</style>
</head>
<body>

<header class="abs site-header">
  <div class="abs site-name">Stock Market</div>
  <span class="abs social" style="left:595px"></span>
  <span class="abs social" style="left:624px"></span>
  <span class="abs social" style="left:653px"></span>
  <span class="abs social" style="left:682px"></span>
  <span class="abs social" style="left:711px"></span>
</header>

<nav class="abs main-nav">
  <div class="nav-links">
    <a>Home</a><a>About</a><a>Categories</a><a>Blog</a><a>Contact Us</a><a>Some Category</a><a>Stock Techniques</a><a>Other Stuff</a>
  </div>
  <div class="abs search">Search this site...
    <svg class="abs" style="right:5px;top:4px" width="10" height="10" viewBox="0 0 10 10"><circle cx="6" cy="4" r="3" fill="none" stroke="#999" stroke-width="1.2"/><line x1="4" y1="6" x2="1" y2="9" stroke="#999" stroke-width="1.4"/></svg>
  </div>
</nav>

<div class="abs dropdown">
  <a>Home</a><a class="dim">About</a><a>Categories</a><a>Shortcodes</a><a>Page Templates</a>
</div>

<section>
  <div class="abs feature-line"></div>
  <div class="abs tab">RECOMMENDED NEWS</div>
  <svg class="abs arrow" style="left:131px" width="14" height="22" viewBox="0 0 14 22"><path d="M11 2 3 11l8 9" fill="none" stroke="#fff" stroke-width="3"/></svg>
  <svg class="abs arrow" style="left:719px" width="14" height="22" viewBox="0 0 14 22"><path d="M3 2l8 9-8 9" fill="none" stroke="#fff" stroke-width="3"/></svg>
  <div class="abs chart" style="left:178px;top:217px;width:210px;height:138px" role="img" aria-label="Stock price chart with volume bars"></div>
  <h2 class="abs feature-title">Post Title Goes Here</h2>
  <div class="abs meta" style="left:414px;top:245px">Reviewed by <b>Admin</b> on March 15, 2011</div>
  <p class="abs excerpt" style="left:414px;top:266px;width:300px;height:86px">Pellentesque tempor dui non mauris ullamcorper sit amet mattis metus dapibus.<br>Vestibulum ante ipsum primis in faucibus orci luctus et ultrices posuere cubilia<br>Pellentesque tempor dui non mauris ullamcorper sit amet mattis metus dapi-<br>bus. Vestibulum ante ipsum primis in faucibus orci luctus et ultrices posuere<br>cubilia Curae; Nullam tristique faucibus gravida. Donec vitae placerat nunc.<br>Nunc ornare odio at augue viverra non fermentum quam imperdiet. Donec</p>
  <div class="abs review-line"></div>
  <div class="abs pill" style="left:372px;top:371px;width:152px;height:20px;line-height:20px;font-size:10.5px">Click to Read The Full Review</div>
</section>

<main>
  <div class="abs label" style="left:132px;top:393px">Recent Posts :</div>

  <article class="abs card" style="left:132px;top:413px">
    <div class="chart" role="img" aria-label="Stock price chart"></div>
    <h3>Post Title Goes Here</h3>
    <div class="meta">Reviewed by <b>Admin</b> on March 15, 2011</div>
    <p class="excerpt">Pellentesque tempor dui non mauris<br>ullamcorper sit amet mattis metus<br>dapibus. Vestibulum ante ipsum<br>primis in faucibus orci luctus et</p>
    <div class="pill">Read More</div>
  </article>
  <div class="abs ribbon">Top Pick</div>

  <article class="abs card" style="left:330px;top:413px">
    <div class="chart" role="img" aria-label="Stock price chart"></div>
    <h3>Post Title Goes Here</h3>
    <div class="meta">Reviewed by <b>Admin</b> on March 15, 2011</div>
    <p class="excerpt">Pellentesque tempor dui non mauris<br>ullamcorper sit amet mattis metus<br>dapibus. Vestibulum ante ipsum<br>primis in faucibus orci luctus et</p>
    <div class="pill">Read More</div>
  </article>

  <article class="abs card" style="left:132px;top:655px">
    <div class="chart" role="img" aria-label="Stock price chart"></div>
    <h3>Post Title Goes Here</h3>
    <div class="meta">Reviewed by <b>Admin</b> on March 15, 2011</div>
    <p class="excerpt">Pellentesque tempor dui non mauris<br>ullamcorper sit amet mattis metus<br>dapibus. Vestibulum ante ipsum<br>primis in faucibus orci luctus et</p>
    <div class="pill">Read More</div>
  </article>

  <article class="abs card" style="left:330px;top:655px">
    <div class="chart" role="img" aria-label="Stock price chart"></div>
    <h3>Post Title Goes Here</h3>
    <div class="meta">Reviewed by <b>Admin</b> on March 15, 2011</div>
    <p class="excerpt">Pellentesque tempor dui non mauris<br>ullamcorper sit amet mattis metus<br>dapibus. Vestibulum ante ipsum<br>primis in faucibus orci luctus et</p>
    <div class="pill">Read More</div>
  </article>

  <div class="abs" style="left:335px;top:930px;font:700 8px 'Droid Serif',serif;white-space:nowrap">Page 1 of 4</div>
  <div class="abs pager" style="left:385px;font-weight:400;color:var(--muted)">1</div>
  <div class="abs pager" style="left:413px">2</div>
  <div class="abs pager" style="left:441px">3</div>
  <div class="abs pager" style="left:469px">4</div>
</main>

<div class="abs side-rule"></div>

<aside>
  <div class="abs newsletter">
    <h4>Subscribe to this newsletter</h4>
    <svg class="abs" style="left:162px;top:12px" width="14" height="10" viewBox="0 0 14 10"><rect width="14" height="10" fill="#444"/><path d="M0 0l7 5 7-5" fill="none" stroke="#fff" stroke-width="1"/></svg>
    <div class="rule"></div>
    <p class="intro">Sign up to receive email updates and to hear what's going on with us!</p>
    <div class="email">Enter E-Mail Address</div>
    <div class="signup">SIGN UP</div>
    <div class="spam"><b>WE HATE SPAM!</b> Really its terrible &amp; we never do it.</div>
  </div>

  <div class="abs label" style="left:543px;top:591px">Links</div>
  <ul class="abs list" style="left:541px;top:608px">
    <li>Rhoncus quis varius sed velit nibh moles</li>
    <li class="dim">Mauris quis nunc eu nunc molestie</li>
    <li>Egestas et sit amet odio morbi quis nunc</li>
    <li>Lacinia velit in nibh sodales sed quis nunc</li>
    <li>Pharetra sem feugiat nibh sodales sed</li>
    <li>Vivamus ut cursus augue nibh sodales sed</li>
  </ul>

  <div class="abs label" style="left:543px;top:714px">Archives</div>
  <ul class="abs list" style="left:541px;top:732px">
    <li>June 2013</li><li>May 2013</li><li>April 2013</li><li>March 2013</li><li>Februaury 2013</li><li>January 2013</li>
  </ul>

  <div class="abs ad">VORTELLI ADVERTISEMENT</div>
</aside>

<footer class="abs site-footer">
  <h5 style="left:132px">ABOUT US</h5>
  <ul class="foot-col" style="left:132px">
    <li>Rhoncus quis varius sed velit nibh moles</li>
    <li>Mauris quis nunc eu nunc molestie</li>
    <li>Egestas et sit amet odio morbi quis nunc</li>
    <li>Lacinia velit in nibh sodales sed quis nunc</li>
    <li>Pharetra sem feugiat nibh sodales sed</li>
    <li>Vivamus ut cursus augue nibh sodales sed</li>
  </ul>
  <h5 style="left:336px">CATEGORIES</h5>
  <ul class="foot-col dots" style="left:336px;top:53px">
    <li>Rhoncus quis varius sed velit nibh moles</li>
    <li>Mauris quis nunc eu nunc molestie</li>
    <li>Egestas et sit amet odio morbi quis nunc</li>
    <li>Lacinia velit in nibh sodales sed quis nunc</li>
    <li>Pharetra sem feugiat nibh sodales sed</li>
    <li>Vivamus ut cursus augue nibh sodales sed</li>
  </ul>
  <h5 style="left:544px">RECENT POSTS</h5>
  <ul class="foot-col dots" style="left:544px;top:53px">
    <li>Rhoncus quis varius sed velit nibh moles</li>
    <li>Mauris quis nunc eu nunc molestie</li>
    <li>Egestas et sit amet odio morbi quis nunc</li>
    <li>Lacinia velit in nibh sodales sed quis nunc</li>
    <li>Pharetra sem feugiat nibh sodales sed</li>
    <li>Vivamus ut cursus augue nibh sodales sed</li>
  </ul>
  <div class="footer-bar">
    <div class="footer-links">
      <a class="current">Home</a><a>About</a><a>Categories</a><a>Shortcodes</a><a>Page Templates</a><a>Blog</a><a>Contact Us</a>
    </div>
  </div>
</footer>

</body>
</html>
```